Business Card

We need some ideas for corporate business cards. I'm interested in a double sided card, with one side featuring our corporate logo, the other side with employee information.

Corporate colors, logo etc. available at www.brivalo.com

Industry/Entity Type

Business

Requirements
Must have
• The "Brivalo" logo with stylized "O"

Nice to have
• Preferred font is calibri

```html
<!DOCTYPE html>
<html lang="en">
<head>
<meta charset="utf-8">
<title>Brivalo Business Card</title>
<link rel="stylesheet" href="https://fonts.googleapis.com/css2?family=Carlito:wght@400;700&display=swap">
<style>
  :root {
    --stage: #000000;
    --paper: #ffffff;
    --brand-blue: #4a6293;
    --brand-navy: #27324b;
    --soft-grey: #e6e6e6;
    --ink: #111111;
    --band-text: #e4e9f3;
  }
  * { margin: 0; padding: 0; box-sizing: border-box; }
  html, body { width: 1000px; height: 1200px; overflow: hidden; background: var(--stage); }
  body { font-family: "Carlito", "Calibri", sans-serif; position: relative; }

  .card { position: absolute; top: 105px; height: 288px; overflow: hidden; }
  .card-front { left: 0; width: 503px; background: var(--paper); }
  .card-back { left: 503px; width: 497px; background: var(--brand-blue); }

  .shape-layer { position: absolute; inset: 0; }

  .front-wordmark {
    position: absolute; left: 335px; top: 52px;
    font-size: 26px; font-weight: 700; letter-spacing: 2px; color: var(--ink);
  }
  .holder { position: absolute; left: 37px; top: 122px; color: var(--brand-blue); }
  .holder-name { font-size: 19px; line-height: 1; }
  .holder-name strong { font-weight: 700; }
  .holder-role { font-size: 11px; font-weight: 700; color: var(--ink); margin-top: 3px; }

  .info-band {
    position: absolute; left: 0; top: 172px; width: 503px; height: 116px;
    background: var(--brand-blue); color: var(--band-text);
  }
  .address { position: absolute; left: 36px; top: 20px; font-size: 10px; line-height: 16px; }
  .address strong { font-weight: 700; color: #ffffff; }
  .contacts { position: absolute; left: 333px; top: 19px; list-style: none; font-size: 10px; }
  .contacts li { display: flex; align-items: center; height: 19.5px; }
  .contacts svg { width: 11px; height: 11px; margin-right: 6px; flex: none; }

  .back-wordmark {
    position: absolute; left: 32px; top: 196px;
    font-size: 62px; font-weight: 700; letter-spacing: 6px; line-height: 1; color: #ffffff;
  }
</style>
</head>
<body>

  <section class="card card-front" aria-label="Card front, employee details">
    <svg class="shape-layer" width="503" height="288" viewBox="0 0 503 288" aria-hidden="true">
      <polygon points="308,0 503,0 503,35 345,35" fill="var(--soft-grey)"/>
      <polygon points="337,93 272,172 402,172" fill="var(--soft-grey)"/>
    </svg>

    <div class="front-wordmark">BRIVALO</div>

    <div class="holder">
      <p class="holder-name"><strong>DANIEL</strong> FERRANTE</p>
      <p class="holder-role">Chairman</p>
    </div>

    <div class="info-band">
      <p class="address">
        <strong>Brivalo Telecom Malaysia</strong><br>
        Level 12, Northgate Tower, Harbour Square, Seri Bay City<br>
        Jalan Seri Mutiara 50450 , KL,<br>
        Malaysia
      </p>
      <ul class="contacts">
        <li>
          <svg viewBox="0 0 12 12" fill="none" stroke="currentColor" stroke-width="1"><rect x="3" y="1" width="6" height="10" rx="1"/><line x1="5" y1="9" x2="7" y2="9"/></svg>
          +1 555 210 4820
        </li>
        <li>
          <svg viewBox="0 0 12 12" fill="none" stroke="currentColor" stroke-width="1"><rect x="2" y="1" width="8" height="10"/><line x1="4" y1="4" x2="8" y2="4"/><line x1="4" y1="6" x2="8" y2="6"/><line x1="4" y1="8" x2="8" y2="8"/></svg>
          +1 555 210 4730
        </li>
        <li>
          <svg viewBox="0 0 12 12" fill="none" stroke="currentColor" stroke-width="1"><rect x="1" y="2.5" width="10" height="7"/><polyline points="1,2.5 6,7 11,2.5"/></svg>
          info@brivalo.com
        </li>
        <li>
          <svg viewBox="0 0 12 12" fill="none" stroke="currentColor" stroke-width="1"><circle cx="6" cy="6" r="5"/><ellipse cx="6" cy="6" rx="2" ry="5"/><line x1="1" y1="6" x2="11" y2="6"/></svg>
          www.brivalo.com
        </li>
      </ul>
    </div>
  </section>

  <section class="card card-back" aria-label="Card back, company name">
    <svg class="shape-layer" width="497" height="288" viewBox="0 0 497 288" aria-hidden="true">
      <polygon points="350,172 497,0 497,288 440,288 440,172" fill="var(--brand-navy)"/>
    </svg>
    <div class="back-wordmark">BRIVALO</div>
  </section>

</body>
</html>
```